Serial Entrepreneur Business Card: 4 Logo Design

I am a serial entrepreneur and a full time mechanical engineer. I have four businesses. I would like to display them all on one business card.
*Please see the attached PDF for the design requirements*

www.KelbroNest.com

Businesses
-KelbroNest
-Quiet Lantern Properties
-Torlen Products
-Drosk Harbor Cast

Target Market(s)

Clients, Entrepreneurs, Associates, really anyone. Should be very professional.

Industry/Entity Type

Entrepreneur

Contact Information for Business Card

3.5" x 2" Standard Business Card Size
** Please review the attached requirement PDF for in depth detail on what I am expecting**

Font styles to use
Sans Serif

Requirements
Must have
• My personal contact information:
• First Name: Dae hwan
• Last Name: Pellow
• Nick Name: Riko
• Address: 83 Tolmer Court, Ashvale ZN 07392
• Phone Number: 555-574-2916
• Email: RikodPellow@mailnest.example
• Website: www.KelbroNest.com
• All Four Logos of the Companies I own:
• -KelbroNest
• -Quiet Lantern Properties
• -Torlen Products
• -Drosk Harbor Cast
• My Professions:
• -Prototyping Engineer
• -Real Estate Investor
• -Financial Blogger
• -Video Podcaster
• -Online Retail Seller
Nice to have
• If it fits, please include the website for each logo, if there is more space please include the email for each.
• It might be nice to have the QX GUILD Logo, or TOVRA logo for my full-time job. But only if it fits.

```html
<!DOCTYPE html>
<html lang="en">
<head>
<meta charset="utf-8">
<title>Dae hwan "Riko" Pellow – Business Card</title>
<link href="https://fonts.googleapis.com/css2?family=Poppins:ital,wght@0,400;0,600;0,700;0,800;1,600&display=swap" rel="stylesheet">
<style>
  :root {
    --green: #0d8a1a;
    --ink: #222222;
    --grey: #555555;
    --paper: #ffffff;
    --backdrop: #ececec;
  }
  * { box-sizing: border-box; margin: 0; padding: 0; }
  html, body { width: 1200px; height: 1200px; overflow: hidden; }
  body {
    background: var(--backdrop);
    font-family: "Poppins", sans-serif;
    color: var(--ink);
    position: relative;
  }
  .card {
    position: absolute;
    left: 180px;
    width: 840px;
    height: 480px;
    background: var(--paper);
    box-shadow: 0 6px 18px rgba(0,0,0,0.18);
    overflow: hidden;
  }
  /* Contact side */
  .card--front { top: 50px; }
  .front__top-band { position: absolute; top: 0; left: 0; right: 0; height: 16px; background: var(--green); }
  .front__bottom-band { position: absolute; bottom: 0; left: 0; right: 0; height: 52px; background: var(--green); }
  .holder-name {
    position: absolute; top: 42px; left: 230px;
    font-size: 40px; font-weight: 700; color: #3a3a3a; letter-spacing: 0.5px; white-space: nowrap;
  }
  .holder-name .nickname { color: var(--green); }
  .professions {
    position: absolute; top: 112px; left: 62px;
    list-style: none; font-size: 17px; font-style: italic; font-weight: 600; line-height: 25px; color: #333;
  }
  .professions li::before { content: "•"; color: var(--green); font-style: normal; margin-right: 9px; }
  .contact {
    position: absolute; top: 178px; left: 420px;
  }
  .contact__line {
    position: absolute; left: 17px; top: 20px; width: 4px; height: 92px; background: var(--green);
  }
  .contact__row { position: relative; display: flex; align-items: center; height: 46px; }
  .contact__icon {
    width: 38px; height: 38px; border-radius: 50%; background: var(--green);
    display: flex; align-items: center; justify-content: center; flex: none;
  }
  .contact__text { margin-left: 18px; font-size: 18px; font-weight: 700; color: #333; white-space: nowrap; }
  .ventures {
    position: absolute; left: 28px; right: 28px; top: 336px;
    display: flex; justify-content: space-between; align-items: flex-end;
  }
  .venture { display: flex; flex-direction: column; align-items: center; }
  .venture__mark { display: flex; align-items: center; gap: 7px; font-size: 16px; font-weight: 800; color: var(--ink); white-space: nowrap; }
  .venture__mark--green { color: var(--green); }
  .venture__square { width: 14px; height: 14px; background: currentColor; flex: none; }
  .venture__circle { width: 14px; height: 14px; border-radius: 50%; background: currentColor; flex: none; }
  .venture__link { margin-top: 8px; font-size: 11px; font-weight: 600; color: #333; white-space: nowrap; }

  /* Logo side */
  .card--back { top: 640px; }
  .back__band { position: absolute; top: 0; bottom: 0; width: 52px; background: var(--green); }
  .back__band--left { left: 0; }
  .back__band--right { right: 0; }
  .brand-stack {
    position: absolute; left: 52px; right: 52px; top: 0; bottom: 0;
    display: flex; justify-content: space-evenly; align-items: center;
  }
  .brand {
    writing-mode: vertical-rl; transform: rotate(180deg);
    display: flex; align-items: center; gap: 14px;
    font-weight: 800; color: var(--ink); line-height: 1.1;
  }
  .brand--green { color: var(--green); }
  .brand__shape { width: 30px; height: 30px; background: currentColor; flex: none; }
  .brand__shape--round { border-radius: 50%; }
  .brand__name { font-size: 40px; white-space: nowrap; }
</style>
</head>
<body>

<section class="card card--front" aria-label="Contact side">
  <div class="front__top-band"></div>
  <h1 class="holder-name">Dae hwan <span class="nickname">“Riko”</span> Pellow</h1>
  <ul class="professions">
    <li>Prototyping Engineer</li>
    <li>Real Estate Investor</li>
    <li>Financial Blogger</li>
    <li>Video Podcaster</li>
    <li>Online Retail Seller</li>
  </ul>
  <div class="contact">
    <div class="contact__line"></div>
    <div class="contact__row">
      <span class="contact__icon">
        <svg width="20" height="20" viewBox="0 0 24 24"><path d="M12 2a7 7 0 0 0-7 7c0 5 7 13 7 13s7-8 7-13a7 7 0 0 0-7-7zm0 9.5A2.5 2.5 0 1 1 12 6.5a2.5 2.5 0 0 1 0 5z" fill="#fff"/></svg>
      </span>
      <span class="contact__text">83 Tolmer Court, Ashvale ZN 07392</span>
    </div>
    <div class="contact__row">
      <span class="contact__icon">
        <svg width="18" height="18" viewBox="0 0 24 24"><rect x="6" y="2" width="12" height="20" rx="2" fill="none" stroke="#fff" stroke-width="2.4"/><circle cx="12" cy="18" r="1.3" fill="#fff"/></svg>
      </span>
      <span class="contact__text">555-574-2916</span>
    </div>
    <div class="contact__row">
      <span class="contact__icon">
        <svg width="20" height="20" viewBox="0 0 24 24"><rect x="3" y="5" width="18" height="14" rx="1.5" fill="#fff"/><path d="M3.5 6l8.5 7 8.5-7" fill="none" stroke="#0d8a1a" stroke-width="2"/></svg>
      </span>
      <span class="contact__text">RikodPellow@mailnest.example</span>
    </div>
  </div>
  <div class="ventures">
    <div class="venture">
      <span class="venture__mark venture__mark--green"><span class="venture__circle"></span>KelbroNest</span>
      <span class="venture__link">www.KelbroNest.com</span>
    </div>
    <div class="venture">
      <span class="venture__mark"><span class="venture__square"></span>Torlen Products</span>
      <span class="venture__link">Sales@TorlenProducts.com</span>
    </div>
    <div class="venture">
      <span class="venture__mark venture__mark--green"><span class="venture__square"></span>Drosk Harbor Cast</span>
      <span class="venture__link">Media@DroskHarborCast.com</span>
    </div>
    <div class="venture">
      <span class="venture__mark"><span class="venture__square"></span>Quiet Lantern Properties</span>
      <span class="venture__link">Riko@QuietLanternProperties.com</span>
    </div>
  </div>
  <div class="front__bottom-band"></div>
</section>

<section class="card card--back" aria-label="Company side">
  <div class="back__band back__band--left"></div>
  <div class="brand-stack">
    <div class="brand brand--green"><span class="brand__shape brand__shape--round"></span><span class="brand__name">KelbroNest</span></div>
    <div class="brand"><span class="brand__shape"></span><span class="brand__name">Torlen Products</span></div>
    <div class="brand brand--green"><span class="brand__shape"></span><span class="brand__name">Drosk Harbor Cast</span></div>
    <div class="brand"><span class="brand__shape"></span><span class="brand__name">Quiet Lantern<br>Properties</span></div>
  </div>
  <div class="back__band back__band--right"></div>
</section>

</body>
</html>
```